Agency Website & Personal brand

My name is Kostas Vranelis & I've been a digital marketer & an e-commerce expert since 2010.

- I've spoken to 20 different events around the world up to 3,000 people in size.
- I've sold over 1500 training courses around e-commerce growth.
- I have over 100 testimonials (video & photo) from successful students who bought my training
- I have dozens of video testimonials from respected entrepreneurs that vouch for me and my work
- I have photos with marketing legends with that I shared the stage like Owen Tarrick, Martin Fellowbrand, Glen Maro & more
- I am the host of the Aegean Roundtable since 2017 - a high-level networking event for 7 & 8 figure entrepreneurs - 100 people have come to Greece since 2017
- I have tons of videos created where I showcase my expertise on growth
- I have worked with dozens of e-commerce stores on their growth & helped them scale to multiple 6, 7 & 8 figures either on consulting

I need a website design that showcases my authority & be a lead generating machine.

The goal is to bring people on a call with me but also grab their email and start building the relationship with them and free valuable content

We have 3 offers :

1. Paid ads (Done for You)
2. Consulting/Mastermind (Done with You)
3. Training (Do it Yourself)

```html
<!DOCTYPE html>
<html lang="en">
<head>
<meta charset="utf-8">
<title>Kostas Vranelis — Digital Marketer & E-Commerce Expert</title>
<link rel="stylesheet" href="https://fonts.googleapis.com/css2?family=Manrope:wght@400;500;600;700;800&display=swap">
<style>
:root{
  --navy:#15174a;
  --indigo:#2d2f96;
  --indigo-deep:#22247a;
  --blue:#2f33a8;
  --ink:#14142b;
  --text:#3a3a4f;
  --muted:#6d6d80;
  --light:#f3f3f6;
  --line:#d9d9e3;
  --white:#ffffff;
  --chip:#2b2b3e;
}
*{box-sizing:border-box;margin:0;padding:0}
html,body{width:1200px;height:5097px;overflow:hidden}
body{font-family:"Manrope",sans-serif;color:var(--text);background:var(--white);font-size:15px;line-height:1.55}
.wrap{width:1072px;margin:0 auto;position:relative;height:100%}
.section{position:relative;overflow:hidden}
.btn{display:inline-block;background:var(--indigo);color:var(--white);font-weight:600;font-size:15px;padding:14px 32px;border-radius:3px;text-decoration:none;white-space:nowrap}
.ph{display:block;border-radius:6px}
.section-title{text-align:center;font-weight:800;font-size:32px;color:var(--indigo);letter-spacing:.3px;text-transform:uppercase}
.play{position:absolute;left:50%;top:50%;transform:translate(-50%,-50%)}

/* nav */
.nav{height:100px;background:var(--white)}
.nav .wrap{display:flex;align-items:center;justify-content:space-between}
.brand{font-weight:800;font-size:22px;color:var(--ink);letter-spacing:.5px}
.menu{display:flex;gap:30px;font-size:15px;font-weight:500;color:var(--ink);list-style:none}
.menu .active{color:var(--indigo);font-weight:700}

/* hero */
.hero{height:412px;background:linear-gradient(100deg,#101245 0%,#1c1f6e 55%,#2a2d8c 100%)}
.hero-photo{position:absolute;left:760px;top:0;width:380px;height:412px;background:linear-gradient(180deg,#3b3f9e,#1a1c5c)}
.hero-copy{position:absolute;left:128px;top:118px;color:var(--white)}
.hero h1{font-size:46px;font-weight:800;line-height:1.1;letter-spacing:.5px;text-transform:uppercase}
.hero p{margin-top:16px;font-size:18px;width:360px;line-height:1.4;color:#e5e6f5}
.hero .btn{margin-top:28px;background:var(--blue);padding:12px 26px}
.social-rail{position:absolute;right:28px;top:122px;display:flex;flex-direction:column;gap:10px}
.social-rail span{width:30px;height:30px;background:var(--chip);border-radius:3px;display:block}

/* about */
.about{height:688px}
.about-photo{position:absolute;left:128px;top:96px;width:400px;height:480px;border-radius:4px;background:linear-gradient(160deg,#c9c4bd,#8c8279)}
.about-copy{position:absolute;left:652px;top:104px;width:430px}
.about h2{font-size:30px;font-weight:800;color:var(--ink);text-transform:uppercase;white-space:nowrap}
.about h2 span{color:var(--indigo)}
.ticks{list-style:none;margin-top:18px}
.ticks li{position:relative;padding-left:24px;font-size:14px;line-height:1.45;margin-bottom:14px;color:var(--text)}
.ticks svg{position:absolute;left:0;top:4px}
.about .btn{margin-top:12px;background:var(--indigo-deep)}

/* offers */
.offers{height:600px;background:linear-gradient(180deg,var(--indigo) 0%,#292c8c 100%)}
.offers .section-title{color:var(--white);padding-top:100px;font-size:30px}
.offer-grid{position:absolute;left:128px;top:180px;display:flex;gap:32px}
.offer{width:292px;height:292px;background:var(--white);border-radius:6px;overflow:hidden}
.offer .ph{height:180px;border-radius:0}
.offer h3{padding:18px 20px 0;font-size:19px;font-weight:800;color:var(--indigo)}
.offer p{padding:2px 20px;font-size:15px;color:var(--text)}

/* case study */
.case{height:440px;background:var(--light)}
.case-copy{position:absolute;left:128px;top:136px;width:370px}
.eyebrow{font-size:14px;font-weight:700;color:var(--indigo);letter-spacing:.5px;text-transform:uppercase}
.case h2{margin-top:6px;font-size:34px;font-weight:800;color:var(--ink);line-height:1.15;text-transform:uppercase}
.case .btn{margin-top:22px;padding:12px 24px;font-size:14px}
.case-video{position:absolute;left:560px;top:64px;width:512px;height:296px;border-radius:8px;background:linear-gradient(135deg,#2b2d6e,#e9eaf3 60%,#ffffff)}

/* events */
.events{height:920px}
.events .section-title{padding-top:92px;color:var(--indigo)}
.ev{position:absolute}
.events .btn{position:absolute;left:496px;top:828px;padding:12px 30px;font-size:14px}

/* testimonials */
.testi{height:740px;background:var(--light)}
.testi .section-title{padding-top:80px}
.testi .sub{text-align:center;font-size:15px;width:520px;margin:10px auto 0;color:var(--text)}
.t-grid{position:absolute;left:128px;top:212px;display:flex;gap:32px}
.t-card{width:302px;height:328px;background:var(--white);border-radius:6px;overflow:hidden}
.t-card .ph{height:180px;border-radius:0;position:relative}
.t-card h3{padding:16px 20px 2px;font-size:18px;font-weight:800;color:var(--indigo)}
.t-card p{padding:0 20px;font-size:14px;color:var(--text)}
.testi .btn{position:absolute;left:476px;top:620px;padding:12px 28px;font-size:14px}

/* blog */
.blog{height:620px}
.blog-head{position:absolute;top:168px;left:128px;width:944px;display:flex;align-items:center;gap:22px}
.blog-head hr{flex:1;border:none;border-top:2px solid var(--indigo)}
.blog-head h2{font-size:32px;font-weight:800;color:var(--indigo);text-transform:uppercase;white-space:nowrap}
.b-grid{position:absolute;left:128px;top:252px;display:flex;gap:32px}
.post{width:292px;text-align:center}
.post .ph{height:128px;border-radius:4px}
.post h3{margin-top:16px;font-size:17px;font-weight:800;color:var(--ink);line-height:1.35}
.blog .btn{position:absolute;left:532px;top:508px;padding:12px 28px;font-size:14px}

/* footer */
.footer{height:460px;background:var(--light)}
.f-col{position:absolute;top:96px}
.f-col h4{font-size:15px;font-weight:800;color:var(--indigo);text-transform:uppercase;margin-bottom:18px}
.f-col ul{list-style:none}
.f-col li{font-size:14px;margin-bottom:10px;color:var(--text)}
.f-col p{font-size:14px;color:var(--text);line-height:1.55}
.field{margin-top:30px;width:346px;height:44px;background:var(--white);border:1px solid var(--line);font-size:14px;padding:12px 14px;color:var(--muted)}
.f-col .btn{display:block;width:346px;text-align:center;margin-top:14px;padding:12px 0;font-size:14px;background:var(--indigo-deep)}

.bottom{height:117px;border-top:1px solid var(--line);background:var(--white)}
.bottom .wrap{display:flex;align-items:center;justify-content:space-between}
.bottom p{font-size:14px;color:var(--ink)}
.social-row{display:flex;gap:10px}
.social-row span{width:32px;height:32px;background:var(--chip);border-radius:3px;display:block}
</style>
</head>
<body>

<header class="section nav">
  <div class="wrap">
    <div class="brand">KOSTAS VRANELIS</div>
    <ul class="menu">
      <li class="active">Home</li><li>About ▾</li><li>Offers</li><li>Resources</li><li>Media</li><li>Blog</li><li>Contact</li>
    </ul>
  </div>
</header>

<section class="section hero">
  <div class="hero-photo" role="img" aria-label="Portrait of Kostas Vranelis in a suit, arms crossed, on a blue stage backdrop"></div>
  <div class="hero-copy">
    <h1>Kostas Vranelis</h1>
    <p>Digital Marketer, E-Commerce Expert, Public Speaker and Trainer.</p>
    <a class="btn">Learn More</a>
  </div>
  <div class="social-rail" aria-label="Social profiles"><span></span><span></span><span></span><span></span><span></span><span></span></div>
</section>

<section class="section about">
  <div class="about-photo" role="img" aria-label="Kostas Vranelis speaking on stage with a microphone"></div>
  <div class="about-copy">
    <h2>About <span>Kostas Vranelis</span></h2>
    <ul class="ticks">
      <li><svg width="14" height="12" viewBox="0 0 14 12"><path d="M1 6l4 4 8-9" fill="none" stroke="#2d2f96" stroke-width="2"/></svg>I am a master at Conversion Rate Optimisation &amp; Scaling, with Statlens Analytics.</li>
      <li><svg width="14" height="12" viewBox="0 0 14 12"><path d="M1 6l4 4 8-9" fill="none" stroke="#2d2f96" stroke-width="2"/></svg>I travel the world to speak at conferences &amp; events up to 3,000 people in size (20 events, 15 countries, 4 continents, 15,000+ live attendees so far).</li>
      <li><svg width="14" height="12" viewBox="0 0 14 12"><path d="M1 6l4 4 8-9" fill="none" stroke="#2d2f96" stroke-width="2"/></svg>I am the host of the Aegean Roundtable, a high-level networking mastermind event held in Greece twice per year (est.2017 - 100+ attendees from 24 countries).</li>
      <li><svg width="14" height="12" viewBox="0 0 14 12"><path d="M1 6l4 4 8-9" fill="none" stroke="#2d2f96" stroke-width="2"/></svg>I've helped 10,000+ people to build &amp; grow their online businesses.</li>
      <li><svg width="14" height="12" viewBox="0 0 14 12"><path d="M1 6l4 4 8-9" fill="none" stroke="#2d2f96" stroke-width="2"/></svg>I've worked with 200+ clients for the past 11 years to scale their eCommerce store to multiple 6, 7 &amp; 8 figures.</li>
    </ul>
    <a class="btn">Well, there's more...</a>
  </div>
</section>

<section class="section offers">
  <h2 class="section-title">What I can do for you</h2>
  <div class="offer-grid">
    <div class="offer"><div class="ph" role="img" aria-label="Laptop on a desk showing ad campaign dashboards" style="background:linear-gradient(135deg,#5a6fb0,#c6d0e8)"></div><h3>Paid Ads</h3><p>(Done for You)</p></div>
    <div class="offer"><div class="ph" role="img" aria-label="Team at a table reviewing charts in a consulting session" style="background:linear-gradient(135deg,#e8e6e1,#9aa0b5)"></div><h3>Consulting/Mastermind</h3><p>(Done with You)</p></div>
    <div class="offer"><div class="ph" role="img" aria-label="Person studying an online training course on a laptop" style="background:linear-gradient(135deg,#b79a7a,#e9dfd2)"></div><h3>Training</h3><p>(Do it Yourself)</p></div>
  </div>
</section>

<section class="section case">
  <div class="case-copy">
    <div class="eyebrow">Case Study</div>
    <h2>10.3 Million Dollars in 75 Days with a Storecraft Store</h2>
    <a class="btn">Book a Strategy Call</a>
  </div>
  <div class="case-video" role="img" aria-label="Video thumbnail: case study on how we scaled this brand to 8 figures during Covid-19, with a sales dashboard">
    <svg class="play" width="64" height="64" viewBox="0 0 64 64"><circle cx="32" cy="32" r="32" fill="#2d2f96"/><path d="M26 20l18 12-18 12z" fill="#fff"/></svg>
  </div>
</section>

<section class="section events">
  <h2 class="section-title">Events I've spoken in across the globe</h2>
  <div class="ev ph" style="left:128px;top:160px;width:420px;height:272px;background:linear-gradient(135deg,#2a2a30,#c9a43a 70%,#3a3a40)" role="img" aria-label="Q&amp;A panel on a conference stage"></div>
  <div class="ev ph" style="left:564px;top:160px;width:508px;height:272px;background:linear-gradient(160deg,#1b2a6a,#3d58b8 55%,#0e1230)" role="img" aria-label="Large conference hall audience facing a lit stage"></div>
  <div class="ev ph" style="left:128px;top:448px;width:292px;height:312px;background:linear-gradient(160deg,#1f7fc8,#bfe1f5)" role="img" aria-label="Kostas on stage in front of a blue event backdrop"></div>
  <div class="ev ph" style="left:432px;top:448px;width:316px;height:312px;background:linear-gradient(160deg,#f0f0f0,#6b6f7a)" role="img" aria-label="Two speakers seated in a fireside chat"></div>
  <div class="ev ph" style="left:764px;top:448px;width:308px;height:312px;background:linear-gradient(160deg,#0d1020,#3d3f6e)" role="img" aria-label="Speaker on a dark stage presenting to the crowd"></div>
  <a class="btn">Go to Media</a>
</section>

<section class="section testi">
  <h2 class="section-title">Testimonials</h2>
  <p class="sub">Hear from successful entrepreneurs around the globe and many of my successfully trained students.</p>
  <div class="t-grid">
    <div class="t-card"><div class="ph" role="img" aria-label="Video testimonial from Glen Maro" style="background:linear-gradient(135deg,#4a4a55,#b9b9c2)"><svg class="play" width="46" height="46" viewBox="0 0 46 46"><circle cx="23" cy="23" r="23" fill="#fff"/><path d="M19 14l13 9-13 9z" fill="#14142b"/></svg></div><h3>Glen Maro</h3><p>Entrepreneur, Author and Investor.</p></div>
    <div class="t-card"><div class="ph" role="img" aria-label="Video testimonial from Ellis Varga" style="background:linear-gradient(135deg,#5b5b66,#c4c4cc)"><svg class="play" width="46" height="46" viewBox="0 0 46 46"><circle cx="23" cy="23" r="23" fill="#fff"/><path d="M19 14l13 9-13 9z" fill="#14142b"/></svg></div><h3>Ellis Varga</h3><p>Award-Winning Speaker and Author.</p></div>
    <div class="t-card"><div class="ph" role="img" aria-label="Video testimonial from Brant Calloway" style="background:linear-gradient(135deg,#3e3e48,#a7a7b3)"><svg class="play" width="46" height="46" viewBox="0 0 46 46"><circle cx="23" cy="23" r="23" fill="#fff"/><path d="M19 14l13 9-13 9z" fill="#14142b"/></svg></div><h3>Brant Calloway</h3><p>Internationally Renowned Speaker</p></div>
  </div>
  <a class="btn">See All Testimonials</a>
</section>

<section class="section blog">
  <div class="blog-head"><hr><h2>Latest from the blog</h2><hr></div>
  <div class="b-grid">
    <div class="post"><div class="ph" role="img" aria-label="Laptop and notebook on a desk" style="background:linear-gradient(135deg,#6fa0c8,#e8eef4)"></div><h3>How to Sell your Knowledge Online</h3></div>
    <div class="post"><div class="ph" role="img" aria-label="Hands holding a smartphone showing a social feed" style="background:linear-gradient(135deg,#c9a98a,#3e3a45)"></div><h3>Using the Best Converting Socialhive audiences to make $136,624.87 in 30 Days</h3></div>
    <div class="post"><div class="ph" role="img" aria-label="Person browsing products on a tablet" style="background:linear-gradient(135deg,#9fb4c8,#f1ede6)"></div><h3>How to find the most Unique Product Ideas that People want</h3></div>
  </div>
  <a class="btn">Go to Blog</a>
</section>

<footer class="section footer">
  <div class="wrap">
    <div class="f-col" style="left:0">
      <h4>Quick Links</h4>
      <ul><li>About</li><li>Testimonials</li><li>Offers</li><li>Contact</li><li>Resources</li><li>Media</li><li>Blog</li><li>Terms of Service</li><li>Privacy Policy</li></ul>
    </div>
    <div class="f-col" style="left:260px">
      <h4>For Inquiries</h4>
      <p>hello@kostasvranelis.com</p>
    </div>
    <div class="f-col" style="left:596px;width:380px">
      <h4>Subscribe to our newsletter</h4>
      <p>Subscribe to Kostas Vranelis to receive exclusive tips on E-commerce, Dropshipping, Online Marketing, Analytics and much more!</p>
      <div class="field">Email Address</div>
      <a class="btn">Subscribe</a>
    </div>
  </div>
</footer>

<div class="section bottom">
  <div class="wrap">
    <p>© Kostas Vranelis. All Rights Reserved.</p>
    <div class="social-row" aria-label="Social profiles"><span></span><span></span><span></span><span></span><span></span><span></span></div>
  </div>
</div>

</body>
</html>
```